Web page for analytics company

Now that I have a new logo, I need a webpage design that will use it to its potential. Am looking for a design that handles presentation and access to data well - like sites with blocks that provide direct access to content without going through a set of menus. More like an infographic. No left/right menu bar.

I want the logo (attached) against a black background, but not text - not a fan of trying to read white text on a dark screen.

The website - torvimbly.com - currently has four pages - home, who we are, by the numbers and a blog.

The site will be done in Squarespace.

My apologies for not responding promptly - big report due today.  I will be online tomorrow with answers and feedback. 

Thanks!

```html
<!DOCTYPE html>
<html lang="en">
<head>
<meta charset="utf-8">
<title>Torvimbly – Gender Equity Analytics</title>
<link href="https://fonts.googleapis.com/css2?family=Michroma&family=Open+Sans:ital,wght@0,400;0,600;1,400&display=swap" rel="stylesheet">
<style>
:root{
  --orange:#f7931e;
  --orange-deep:#c9650a;
  --black:#000;
  --ink:#222;
  --text:#777;
  --paper:#ececec;
  --white:#fff;
  --dark-btn:#3a3a3a;
  --rule:#cfcfcf;
}
*{box-sizing:border-box;margin:0;padding:0}
html,body{width:678px;height:1200px;overflow:hidden}
body{position:relative;background:var(--paper);font-family:"Open Sans",Verdana,sans-serif;color:var(--text)}
.abs{position:absolute}
.display{font-family:"Michroma",sans-serif;letter-spacing:1px}

/* header */
.site-header{left:0;top:0;width:678px;height:84px;background:var(--black);border-top:2px solid var(--orange)}
.brand{left:42px;top:22px;display:flex;align-items:center;gap:8px;color:var(--white);font-size:21px;font-weight:600}
.brand-dot{width:32px;height:32px;border-radius:50%;background:var(--orange)}
.phone{right:33px;top:10px;color:var(--white);font-size:11px;letter-spacing:1px;display:flex;align-items:center;gap:5px}
.search{left:525px;top:35px;width:120px;height:19px;background:var(--white);border:1px solid #bbb;border-radius:2px;font-size:7px;color:#999;padding:5px 6px}
.main-nav{z-index:5;left:33px;top:72px;width:615px;height:23px;border-radius:7px;background:linear-gradient(#5a5a5a,#2c2c2c);display:flex;align-items:center;padding-left:21px}
.main-nav a{font-family:"Michroma",sans-serif;color:var(--white);font-size:8px;letter-spacing:1px;text-decoration:none;margin-right:28px;line-height:1}
.social{z-index:6;right:38px;top:76px;display:flex;gap:5px}
.social span{width:15px;height:15px;border-radius:50%;background:var(--white)}

/* hero */
.hero{z-index:1;left:0;top:84px;width:678px;height:223px;background:linear-gradient(120deg,var(--orange-deep),#c86a12 60%,#d2791e)}
.hero-art{left:65px;top:31px;width:165px;height:192px;background:linear-gradient(#1a1a1a,#000);border-radius:60px 60px 0 0}
.quote{left:257px;top:40px;width:360px;color:var(--white)}
.quote h2{font-family:"Michroma",sans-serif;font-size:11px;line-height:16px;letter-spacing:.6px;white-space:nowrap}
.quote p{font-size:7.6px;line-height:13px;letter-spacing:.5px;margin-top:11px;width:350px}
.quote cite{display:block;font-size:7.6px;margin-top:8px}

/* section titles */
.section-title{left:0;width:678px;text-align:center;font-size:11px}
.section-title .accent{color:var(--orange)}
.section-title .dark{color:var(--ink)}
.rule{left:42px;width:588px;height:1px;background:var(--rule)}
.rule-mark{left:332px;width:12px;height:12px;border-radius:50%;background:var(--orange)}

/* features */
.feature{width:150px;text-align:center}
.feature .icon{height:50px;display:flex;align-items:flex-end;justify-content:center}
.feature h3{font-family:"Michroma",sans-serif;font-size:7.5px;color:var(--ink);letter-spacing:1px;margin-top:12px;line-height:10px}
.feature p{font-size:8px;line-height:12px;color:#888;margin:12px 0 0 22px;width:118px;text-align:left}
.btn{display:inline-block;font-size:7px;letter-spacing:.5px;color:var(--white);padding:3px 6px;background:var(--dark-btn);white-space:nowrap}
.btn.hot{background:var(--orange)}
.feature .btn{margin-top:12px}

/* intro */
.intro{left:54px;top:574px;width:565px;height:140px;background:var(--white);border-bottom:4px solid #ccc;padding:13px 38px 0 39px}
.intro p{font-size:7.8px;line-height:12.5px;color:#888;margin-bottom:13px}
.intro .btn{font-size:8px;padding:5px 9px;margin-top:-3px}

/* blog */
.card{top:807px;width:175px;height:196px;background:var(--white);border-bottom:3px solid #ccc}
.card-photo{width:175px;height:105px;background:linear-gradient(#2e4a8a,#3b3e66 55%,#8a5a3a)}
.card-body{padding:6px 5px 0 6px}
.card h4{font-family:"Michroma",sans-serif;font-size:5.6px;color:var(--ink);letter-spacing:.3px;white-space:nowrap}
.meta{font-size:6.5px;color:#777;margin-top:3px}
.card p{font-size:7px;line-height:10px;color:#999;margin-top:3px}
.card .actions{margin-top:7px;display:flex;gap:2px}
.card .btn{font-size:6px;padding:4px 10px}

/* footer */
.site-footer{left:0;top:1040px;width:678px;height:136px;background:var(--black)}
.footer-rule{left:0;top:1082px;width:678px;height:1px;background:#222}
.footer-head{font-family:"Michroma",sans-serif;color:var(--white);font-size:8.5px;letter-spacing:1px}
.qlinks a{display:block;color:var(--white);font-size:8.5px;letter-spacing:.6px;text-decoration:none;margin-bottom:8px}
.qlinks a::before{content:"› ";color:var(--orange);font-weight:600}
.connect div{display:flex;align-items:center;gap:8px;color:var(--white);font-size:8.5px;letter-spacing:.6px;margin-bottom:6px}
.connect span{width:14px;height:14px;border-radius:50%;background:var(--orange)}
.foot-brand{left:262px;top:1096px;display:flex;align-items:center;gap:7px;color:var(--white);font-size:18px;font-weight:600}
.foot-brand .brand-dot{width:28px;height:28px}
.legal{left:0;top:1176px;width:678px;height:24px;background:var(--orange);color:var(--white);font-size:7px;letter-spacing:1px;font-variant:small-caps}
.legal .left{position:absolute;left:76px;top:7px}
.legal .right{position:absolute;right:61px;top:7px}
</style>
</head>
<body>

<header class="abs site-header"></header>
<div class="abs brand"><span class="brand-dot"></span>Torvimbly</div>
<div class="abs phone">
  <svg width="9" height="9" viewBox="0 0 10 10"><rect width="10" height="10" rx="1.5" fill="#f7931e"/><path d="M3 2.5c0 3 1.5 4.5 4.5 4.5l.5-1-1.3-.6-.5.6C5.5 5.5 4.5 4.5 4 3.8l.6-.5L4 2z" fill="#000"/></svg>
  555-203-0147
</div>
<div class="abs search">Keyword Search...
  <svg class="abs" style="right:5px;top:4px" width="10" height="10" viewBox="0 0 10 10"><circle cx="4" cy="4" r="3" fill="none" stroke="#999" stroke-width="1.2"/><line x1="6.2" y1="6.2" x2="9" y2="9" stroke="#999" stroke-width="1.6"/></svg>
</div>

<section class="abs hero">
  <div class="abs hero-art" role="img" aria-label="Illustration of a woman and a man in silhouette, back to back, holding balanced scales"></div>
  <div class="abs quote">
    <h2>"WE KEEP STATISTICS ON EVERYTHING<br>WE CARE ABOUT, FROM RBIS TO ROI,<br>THE DAILY UPS AND DOWNS OF THE<br>DOW AND OUR BANK ACCOUNTS...</h2>
    <p>SO IF WE'RE SERIOUS ABOUT NARROWING THE GENDER GAP AND HELPING MORE GIRLS AND WOMEN, THEN WE MUST GET SERIOUS ABOUT GATHERING AND ANALYZING THE DATA THAT TELL THE TALE."</p>
    <cite>- Former Secretary of State Elena Marsh Whitcombe, July 2012</cite>
  </div>
</section>

<nav class="abs main-nav">
  <a href="#">HOME</a><a href="#">BY THE NUMBERS</a><a href="#">WHO WE ARE</a><a href="#">BLOG</a><a href="#">CONTACT</a>
</nav>
<div class="abs social"><span></span><span></span><span></span></div>

<h2 class="abs section-title display" style="top:332px"><span class="accent">GENDER</span> <span class="dark">EQUITY</span> <span class="accent">ANALYTICS</span></h2>
<div class="abs rule" style="top:355px"></div>
<div class="abs rule-mark" style="top:351px"></div>

<div class="abs feature" style="left:80px;top:382px">
  <div class="icon"><svg width="72" height="44" viewBox="0 0 72 44"><circle cx="19" cy="11" r="7" fill="#222"/><path d="M6 40c0-12 6-16 13-16s13 4 13 16z" fill="#222"/><circle cx="53" cy="11" r="7" fill="#222"/><path d="M40 40c0-12 6-16 13-16s13 4 13 16z" fill="#222"/><circle cx="36" cy="10" r="9" fill="#f7931e"/><path d="M20 42c0-14 7-19 16-19s16 5 16 19z" fill="#f7931e"/></svg></div>
  <h3>WHO WE ARE</h3>
  <p>Lorem ipsum dolor sit amet, consectetur adipiscing elit. Ut felis ligula, dignissim sit amet interdum non lobortis.</p>
  <span class="btn">READ MORE ›</span>
</div>
<div class="abs feature" style="left:262px;top:382px">
  <div class="icon"><svg width="50" height="50" viewBox="0 0 50 50"><rect x="2" y="6" width="46" height="42" rx="3" fill="#222"/><rect x="7" y="16" width="36" height="27" fill="#fff"/><g fill="#f7931e"><rect x="10" y="19" width="6" height="5"/><rect x="18" y="19" width="6" height="5"/><rect x="26" y="19" width="6" height="5"/><rect x="34" y="19" width="6" height="5"/><rect x="10" y="26" width="6" height="5"/><rect x="18" y="26" width="6" height="5"/><rect x="26" y="26" width="6" height="5"/><rect x="34" y="26" width="6" height="5"/><rect x="10" y="33" width="6" height="5"/><rect x="18" y="33" width="6" height="5"/><rect x="26" y="33" width="6" height="5"/></g><rect x="12" y="1" width="4" height="10" rx="2" fill="#222"/><rect x="34" y="1" width="4" height="10" rx="2" fill="#222"/></svg></div>
  <h3>BY THE NUMBERS</h3>
  <p>Lorem ipsum dolor sit amet, consectetur adipiscing elit. Ut felis ligula, dignissim sit amet interdum non lobortis.</p>
  <span class="btn hot">READ MORE ›</span>
</div>
<div class="abs feature" style="left:446px;top:382px">
  <div class="icon"><svg width="50" height="48" viewBox="0 0 50 48"><path d="M2 14c0-8 46-8 46 0v5h-10v-4H12v4H2z" fill="#222"/><path d="M8 22h34l4 24H4z" fill="#222"/><rect x="13" y="24" width="24" height="17" fill="#f7931e"/><path d="M13 24l12 9 12-9" fill="none" stroke="#222" stroke-width="1.5"/></svg></div>
  <h3>CONTACT US</h3>
  <p>Lorem ipsum dolor sit amet, consectetur adipiscing elit. Ut felis ligula, dignissim sit amet interdum non lobortis.</p>
  <span class="btn">READ MORE ›</span>
</div>

<section class="abs intro">
  <p>As much as we'd like to think that treating everyone equally is the best strategy for fairness, the reality is that the differences in the lives of women and men have to be taken into account to ensure that organizations, programs, services, and yes, even public policy treat women and men in ways that achieve gender equity.</p>
  <p>That's where Torvimbly - Gender Equity Analytics - comes in. Using the data-driven tools of gender analysis, we can help you determine if gender equity is being achieved - in businesses and organizations, in the planning and implementation of programs and services, and in the development and enforcement of public policy.</p>
  <span class="btn hot">Read more ›</span>
</section>

<h2 class="abs section-title display" style="top:748px"><span class="accent">OUR</span> <span class="dark">LATEST</span> <span class="accent">BLOG</span></h2>
<div class="abs rule" style="top:771px"></div>
<div class="abs rule-mark" style="top:767px"></div>

<article class="abs card" style="left:54px">
  <div class="card-photo" role="img" aria-label="Photo of women on a conference stage waving to the audience"></div>
  <div class="card-body">
    <h4>TITLE OF THE ARTICLE GOES HERE</h4>
    <div class="meta">▦ March 18, 2014 &nbsp;&nbsp; ▬ Comments (2)</div>
    <p>Lorem ipsum dolor sit amet, consectetur adipiscing elit. Sed tempor feugiat nulla, iaculis egestas ipsum condimentum nec.</p>
    <div class="actions"><span class="btn hot">READ MORE</span><span class="btn">SHARE TO A FRIEND</span></div>
  </div>
</article>
<article class="abs card" style="left:247px">
  <div class="card-photo" role="img" aria-label="Photo of women on a conference stage waving to the audience"></div>
  <div class="card-body">
    <h4>TITLE OF THE ARTICLE GOES HERE</h4>
    <div class="meta">▦ March 18, 2014 &nbsp;&nbsp; ▬ Comments (2)</div>
    <p>Lorem ipsum dolor sit amet, consectetur adipiscing elit. Sed tempor feugiat nulla, iaculis egestas ipsum condimentum nec.</p>
    <div class="actions"><span class="btn hot">READ MORE</span><span class="btn">SHARE TO A FRIEND</span></div>
  </div>
</article>
<article class="abs card" style="left:440px">
  <div class="card-photo" role="img" aria-label="Photo of women on a conference stage waving to the audience"></div>
  <div class="card-body">
    <h4>TITLE OF THE ARTICLE GOES HERE</h4>
    <div class="meta">▦ March 18, 2014 &nbsp;&nbsp; ▬ Comments (2)</div>
    <p>Lorem ipsum dolor sit amet, consectetur adipiscing elit. Sed tempor feugiat nulla, iaculis egestas ipsum condimentum nec.</p>
    <div class="actions"><span class="btn hot">READ MORE</span><span class="btn">SHARE TO A FRIEND</span></div>
  </div>
</article>

<footer class="abs site-footer"></footer>
<div class="abs footer-rule"></div>
<div class="abs footer-head" style="left:79px;top:1063px">QUICKLINKS</div>
<div class="abs qlinks" style="left:76px;top:1091px"><a href="#">Home</a><a href="#">By the numbers</a><a href="#">Who we are</a></div>
<div class="abs qlinks" style="left:173px;top:1091px"><a href="#">Blog</a><a href="#">Contact</a></div>
<div class="abs foot-brand"><span class="brand-dot"></span>Torvimbly</div>
<div class="abs footer-head" style="left:466px;top:1063px">CONNECT WITH US</div>
<div class="abs connect" style="left:472px;top:1090px">
  <div><span></span>Chirpnet</div>
  <div><span></span>Friendbase</div>
  <div><span></span>Linkwork</div>
</div>
<div class="abs legal"><span class="left">FAQ - Sitemap - Privacy Policy</span><span class="right">Copyright © 2014 Torvimbly</span></div>

</body>
</html>
```